Business Card for a Jewellery Brand

Business card for an upscale jewellery brand. Attached is the brand logo and icon and color board. I am looking for two card versions: one for the founder and one is generic. The card should be elegant and convey upscale and premium feel. I am open to both square and rectangle card shapes.

Industry/Entity Type

Jewelry

Contact Information for Business Card

Two cards: (1) Suneha Parmeshwar (Founder) (2) General
(1) Suneha Parmeshwar card should have Name: Suneha Parmeshwar, Title: Founder Email id: suneha@quelm.com.au. Phone no: +61452190437
(2) Generic card should have Email id: info@quelm.com.au. Phone no: +61431267508

Requirements
Must have
• Workmark
• ICON
• Phone no
• Email ID
• ABN: 48291175034 (Note: ABN is Business number in Australia)
• Website: www.quelm.com.au
• Instagram: quelm_jewellery
• Facebook: @quelmjewellery
Nice to have
• Tagline

```html
<!DOCTYPE html>
<html lang="en">
<head>
<meta charset="utf-8">
<title>QUELM Business Cards</title>
<link rel="stylesheet" href="https://fonts.googleapis.com/css2?family=Didact+Gothic&display=swap">
<style>
  :root {
    --backdrop: #3b3b3b;
    --card-white: #ffffff;
    --rose: #e79a91;
    --rose-light: #ec9f94;
    --ink: #3f3f3f;
    --rule: #b9b9b9;
    --font: "Didact Gothic", "Century Gothic", sans-serif;
  }
  * { box-sizing: border-box; margin: 0; padding: 0; }
  html, body { width: 1200px; height: 900px; overflow: hidden; }
  body { background: var(--backdrop); font-family: var(--font); color: var(--ink); position: relative; }

  .card {
    position: absolute;
    width: 513px;
    height: 296px;
    border-radius: 28px;
    overflow: hidden;
  }
  .card--front { left: 344px; top: 138px; }
  .card--founder { left: 73px; top: 465px; background: var(--card-white); }
  .card--general { left: 616px; top: 465px; background: var(--card-white); }

  .front-pattern {
    position: absolute; inset: 0;
    background:
      linear-gradient(115deg, transparent 0 30%, rgba(236,159,148,.55) 30% 36%, transparent 36%),
      linear-gradient(65deg, transparent 0 64%, rgba(236,159,148,.55) 64% 70%, transparent 70%),
      linear-gradient(180deg, #e6968d 0%, #d6828a 100%);
  }
  .front-mark {
    position: absolute; left: 0; right: 0; top: 108px;
    display: flex; flex-direction: column; align-items: center; gap: 12px;
  }
  .mark-dot { width: 22px; height: 22px; border-radius: 50%; }
  .front-mark .mark-dot { background: var(--card-white); }
  .wordmark {
    font-family: var(--font); font-size: 30px; letter-spacing: 9px;
    padding-left: 9px; line-height: 1;
  }
  .front-mark .wordmark { color: var(--card-white); }

  .brand {
    position: absolute; left: 0; right: 0; top: 62px;
    display: flex; flex-direction: column; align-items: center; gap: 12px;
  }
  .brand .mark-dot { background: var(--rose); }
  .brand .wordmark { color: var(--rose); }

  .person {
    position: absolute; left: 0; right: 0; top: 140px;
    text-align: center; font-size: 14px; letter-spacing: .3px;
    display: flex; justify-content: center; align-items: center; gap: 6px;
  }
  .person svg { width: 14px; height: 14px; }

  .rule { position: absolute; left: 34px; right: 34px; height: 1px; background: var(--rule); }
  .rule--top { top: 167px; }
  .rule--icons { top: 204px; }
  .rule--rose { top: 240px; background: var(--rose); opacity: .7; }

  .tagline {
    position: absolute; left: 60px; right: 60px; top: 176px;
    display: flex; justify-content: space-between;
    font-size: 16px; line-height: 1;
  }

  .contact-icon {
    position: absolute; top: 197px; width: 24px; height: 14px;
    background: var(--card-white); display: flex; justify-content: center; align-items: center;
    transform: translateX(-50%);
  }
  .contact-icon svg { width: 13px; height: 13px; }
  .contacts { position: absolute; left: 0; right: 0; top: 215px; font-size: 12.5px; }
  .contacts span { position: absolute; transform: translateX(-50%); white-space: nowrap; }
  .col-1 { left: 119px; }
  .col-2 { left: 257px; }
  .col-3 { left: 393px; }

  .socials {
    position: absolute; left: 0; right: 0; top: 251px;
    display: flex; justify-content: center; gap: 12px; font-size: 12.5px;
    white-space: nowrap;
  }
  .social { display: flex; align-items: center; gap: 4px; }
  .social-square { width: 12px; height: 12px; background: var(--rose); border-radius: 2px; }
  .social-circle { width: 12px; height: 12px; border: 1.5px solid var(--rose); border-radius: 50%; }
  .abn { position: absolute; left: 0; right: 0; top: 270px; text-align: center; font-size: 11px; color: var(--ink); letter-spacing: .3px; }
</style>
</head>
<body>

  <section class="card card--front">
    <div class="front-pattern" role="img" aria-label="Faceted rose-pink gem-ray pattern"></div>
    <div class="front-mark">
      <span class="mark-dot"></span>
      <span class="wordmark">QUELM</span>
    </div>
  </section>

  <section class="card card--founder">
    <div class="brand">
      <span class="mark-dot"></span>
      <span class="wordmark">QUELM</span>
    </div>
    <p class="person">
      <svg viewBox="0 0 14 14"><circle cx="7" cy="7" r="7" fill="#e79a91"/><circle cx="7" cy="5.3" r="2.3" fill="#fff"/><path d="M3 11.2c.8-2 2.3-3 4-3s3.2 1 4 3" fill="#fff"/></svg>
      <span>SUNEHA PARMESHWAR | founder</span>
    </p>
    <div class="rule rule--top"></div>
    <div class="tagline"><span>T</span><span>A</span><span>G</span><span>L</span><span>I</span><span>N</span><span>E</span></div>
    <div class="rule rule--icons"></div>
    <span class="contact-icon col-1"><svg viewBox="0 0 13 13"><rect x="1" y="3" width="11" height="8" fill="#e79a91"/><path d="M1 3l5.5 4.5L12 3" stroke="#fff" fill="none"/></svg></span>
    <span class="contact-icon col-2"><svg viewBox="0 0 13 13"><path d="M3 1.5h2l1 3-1.3 1a7 7 0 0 0 3 3l1-1.3 3 1v2a1.3 1.3 0 0 1-1.4 1.3A10 10 0 0 1 1.7 3 1.3 1.3 0 0 1 3 1.5z" fill="#e79a91"/></svg></span>
    <span class="contact-icon col-3"><svg viewBox="0 0 13 13"><circle cx="6.5" cy="6.5" r="5.5" fill="none" stroke="#e79a91" stroke-width="1.3"/><ellipse cx="6.5" cy="6.5" rx="2.3" ry="5.5" fill="none" stroke="#e79a91"/><path d="M1 6.5h11M2 3.8h9M2 9.2h9" stroke="#e79a91"/></svg></span>
    <div class="contacts">
      <span class="col-1">suneha@quelm.com.au</span>
      <span class="col-2">+61 452 190 437</span>
      <span class="col-3">www.quelm.com.au</span>
    </div>
    <div class="rule rule--rose"></div>
    <div class="socials">
      <span class="social"><span class="social-square"></span>@quelmjewellery</span>
      <span class="social"><span class="social-circle"></span>quelm_jewellery</span>
    </div>
    <p class="abn">ABN 48 291 175 034</p>
  </section>

  <section class="card card--general">
    <div class="brand">
      <span class="mark-dot"></span>
      <span class="wordmark">QUELM</span>
    </div>
    <div class="rule rule--top"></div>
    <div class="tagline"><span>T</span><span>A</span><span>G</span><span>L</span><span>I</span><span>N</span><span>E</span></div>
    <div class="rule rule--icons"></div>
    <span class="contact-icon col-1"><svg viewBox="0 0 13 13"><rect x="1" y="3" width="11" height="8" fill="#e79a91"/><path d="M1 3l5.5 4.5L12 3" stroke="#fff" fill="none"/></svg></span>
    <span class="contact-icon col-2"><svg viewBox="0 0 13 13"><path d="M3 1.5h2l1 3-1.3 1a7 7 0 0 0 3 3l1-1.3 3 1v2a1.3 1.3 0 0 1-1.4 1.3A10 10 0 0 1 1.7 3 1.3 1.3 0 0 1 3 1.5z" fill="#e79a91"/></svg></span>
    <span class="contact-icon col-3"><svg viewBox="0 0 13 13"><circle cx="6.5" cy="6.5" r="5.5" fill="none" stroke="#e79a91" stroke-width="1.3"/><ellipse cx="6.5" cy="6.5" rx="2.3" ry="5.5" fill="none" stroke="#e79a91"/><path d="M1 6.5h11M2 3.8h9M2 9.2h9" stroke="#e79a91"/></svg></span>
    <div class="contacts">
      <span class="col-1">info@quelm.com.au</span>
      <span class="col-2">+61 431 267 508</span>
      <span class="col-3">www.quelm.com.au</span>
    </div>
    <div class="rule rule--rose"></div>
    <div class="socials">
      <span class="social"><span class="social-square"></span>@quelmjewellery</span>
      <span class="social"><span class="social-circle"></span>quelm_jewellery</span>
    </div>
    <p class="abn">ABN 48 291 175 034</p>
  </section>

</body>
</html>
```